Home Health Care Agency Needs a Website (Seeking a PSD)

We need a user friendly website for a Home Health Care Agency. Our service is for the elderly and disabled. Frequently the busy professional middle-aged married daughter will use the website to arrange in-home care for an aging parent. Therefore, our website is primarily geared towards middle-aged women. In-home care is typically 24 hours a day so, a feeling of trustworthiness and security should be effectively conveyed. (Seeking a PSD- however, if you also offer coding, please let us know the cost.)

Target Market(s)

Frequently the busy professional middle-aged married daughter (possibly out of state) will use the website to arrange in-home care for an aging parent.

Industry/Entity Type

Security

Requirements
Must have
• Website must be clean, uncluttered and professional. The following menu pages are requested: Home, About Us, Services, Resources, FAQ, Employment & Contact.
Should not have
• Must not be too whimsical.

```html
<!DOCTYPE html>
<html lang="en">
<head>
<meta charset="utf-8">
<title>Hearthside Home Care</title>
<link href="https://fonts.googleapis.com/css2?family=Open+Sans:ital,wght@0,400;0,600;1,400&family=Roboto:ital,wght@0,400;0,500;0,700;1,400&display=swap" rel="stylesheet">
<style>
:root{
  --blue:#2f9cc8;
  --blue-dark:#1d6d8f;
  --navy:#1f5068;
  --orange:#e0531c;
  --ink:#3d4147;
  --muted:#7d8288;
  --line:#d5dde2;
  --page:#f4f5f6;
  --topbar:#4b4e53;
  --footer:#58595d;
  --footer-dark:#3c3d40;
  --white:#ffffff;
}
*{box-sizing:border-box;margin:0;padding:0}
html,body{width:1200px;height:2311px;overflow:hidden}
body{position:relative;background:var(--page);font-family:"Roboto",Arial,sans-serif;color:var(--ink)}
.abs{position:absolute}
a{color:inherit;text-decoration:none}

/* top bar */
.topbar{left:0;top:0;width:1200px;height:32px;background:var(--topbar);color:#d7d9dc;font-size:11px}
.topbar .item{top:9px;display:flex;align-items:center;gap:8px}
.topbar svg{width:11px;height:11px;fill:#c9ccd0}
.social{display:flex;gap:5px}
.social span{width:13px;height:13px;background:var(--blue);border-radius:2px;display:block}

/* header */
.header{left:0;top:32px;width:1200px;height:106px;background:#fbf9f9}
.brand{left:187px;top:52px;display:flex;align-items:center;gap:8px;font-family:"Roboto",sans-serif;font-weight:700;font-size:22px;color:var(--blue);line-height:1.05}
.brand .mark{width:22px;height:22px;border-radius:50%;background:var(--blue);flex:none}
.nav{left:377px;top:71px;display:flex;height:40px;font-size:13px;font-weight:500;color:#2b2f34}
.nav a{display:flex;align-items:center;padding:0 18px;text-transform:uppercase;letter-spacing:.2px}
.nav a.active{background:var(--blue);color:#fff}
.header-rule{left:0;top:138px;width:1200px;height:8px;background:var(--blue);border-top:3px solid #a8d8ec}

/* hero */
.hero{left:0;top:146px;width:1200px;height:446px;background:linear-gradient(90deg,#c7b9ad 0%,#e9e3dc 30%,#d9d4cd 55%,#b8b5ad 75%,#8f9a93 100%)}
.hero-caption{left:172px;top:375px;height:45px;padding:0 12px;background:rgba(40,44,48,.78);color:#fff;font-size:22px;display:flex;align-items:center}
.hero-sub{left:178px;top:428px;width:270px;color:#fff;font-size:12.5px;line-height:1.45}
.hero-arrow{top:338px;width:46px;height:46px;border-radius:50%;background:rgba(50,55,60,.7);display:flex;align-items:center;justify-content:center}
.hero-arrow svg{width:14px;height:14px;stroke:#fff;stroke-width:2.5;fill:none}
.hero-bar{left:0;top:586px;width:1200px;height:6px;background:var(--blue)}

.appointment{left:172px;top:524px;width:856px;height:143px;background:var(--white);border:1px solid #bfd4de}
.appointment h1{position:absolute;left:24px;top:36px;font-family:"Open Sans",sans-serif;font-weight:400;font-size:30px;line-height:1.25;color:#555a60}
.btn-appoint{position:absolute;left:559px;top:47px;width:245px;height:45px;background:var(--orange);color:#fff;font-size:17px;font-weight:500;display:flex;align-items:center;justify-content:center;gap:10px;text-transform:uppercase}
.btn-appoint svg{width:14px;height:14px;fill:#fff}

/* features */
.feature{top:725px;width:260px}
.feature .icon{position:absolute;left:0;top:4px;width:36px;height:36px;border-radius:50%;background:var(--blue-dark);display:flex;align-items:center;justify-content:center}
.feature .icon svg{width:18px;height:18px;fill:#fff}
.feature h3{position:absolute;left:54px;top:6px;width:170px;font-size:16px;font-weight:500;line-height:1.3;color:#3a3e43}
.feature p{position:absolute;left:34px;top:62px;width:190px;font-size:12px;line-height:1.5;color:var(--muted)}
.btn-more{display:inline-flex;align-items:center;justify-content:center;height:19px;padding:0 9px;background:var(--blue);color:#fff;font-size:10.5px;font-weight:500;letter-spacing:.3px}
.feature .btn-more{position:absolute;left:34px;top:132px;width:52px}

.caregiver{left:172px;top:935px;width:856px;height:59px;background:#fff;border:1px solid #b7cfdc}
.caregiver p{position:absolute;left:44px;top:16px;font-family:"Open Sans",sans-serif;font-style:italic;font-size:20px;letter-spacing:1px;color:#555a60;text-transform:uppercase}
.btn-apply{position:absolute;left:707px;top:19px;width:117px;height:21px;background:var(--navy);color:#fff;font-size:10px;font-weight:700;display:flex;align-items:center;justify-content:center;letter-spacing:.4px}

.intro{left:172px;top:1026px;width:856px;text-align:center;font-size:18.5px;font-weight:500;line-height:1.4;color:#4a4f55}

/* cards */
.card{top:1116px;width:188px}
.card .photo{width:188px;height:170px;border:4px solid #fff;box-shadow:0 0 0 1px #dfe3e6}
.card h4{margin-top:24px;width:172px;font-size:14.5px;font-weight:500;line-height:1.35;color:#34383d;min-height:62px}
.card p{margin-top:6px;width:180px;font-size:12px;line-height:1.5;color:var(--muted);height:58px}
.card .btn-more{margin-top:6px;width:52px}

/* panels */
.panel{top:1515px;width:410px;height:378px;background:#fff;border:1px solid #d0d6da;border-radius:3px}
.panel-head{height:55px;border-bottom:1px solid #e2e6e9;display:flex;align-items:center;justify-content:space-between;padding:0 18px}
.panel-head h2{font-size:16px;font-weight:500;letter-spacing:.5px;color:#3a3e43}
.btn-follow{height:20px;padding:0 9px;border:1px solid #c9cfd3;border-radius:3px;font-size:10px;display:flex;align-items:center;color:#444;background:#f7f8f9}
.btn-view{height:19px;width:86px;background:var(--blue);color:#fff;font-size:10.5px;font-weight:500;display:flex;align-items:center;justify-content:center}
.tweet{position:absolute;left:16px;width:380px}
.tweet .who{position:absolute;left:0;top:0;width:90px;display:flex;align-items:center;gap:4px;font-weight:700;font-size:12px;color:var(--blue);line-height:1.05}
.tweet .who i{width:8px;height:8px;background:var(--blue);display:block;flex:none}
.tweet .body{position:absolute;left:92px;top:0;width:285px;font-size:12px;line-height:1.55;color:#5b6066}
.tweet .body b{font-weight:500;color:#3a3e43;font-size:13px}
.tweet .date{position:absolute;right:12px;top:0;font-size:10.5px;color:#7a7f85}
.tweet .meta{font-size:10.5px;color:#9aa0a5;display:block;margin-top:2px}
.news{position:absolute;left:18px;width:375px}
.news .thumb{position:absolute;left:0;top:0;width:55px;height:48px;background:linear-gradient(135deg,#e6c9b8,#a8a39c)}
.news .date{position:absolute;left:55px;top:0;width:50px;height:48px;background:var(--blue);color:#fff;font-size:8.5px;font-weight:700;text-align:center;display:flex;align-items:center;justify-content:center;line-height:1.3}
.news h5{position:absolute;left:127px;top:0;width:220px;font-size:14px;font-weight:500;line-height:1.35;color:#3a3e43}
.news small{position:absolute;left:127px;top:42px;font-size:9px;color:#9aa0a5}
.news p{position:absolute;left:0;top:70px;width:370px;font-size:11.5px;line-height:1.55;color:#5b6066}

/* footer */
.footer{left:0;top:1938px;width:1200px;height:307px;background:var(--footer);color:#e4e5e6}
.fcol{position:absolute;top:47px}
.fcol h6{font-size:14.5px;font-weight:700;letter-spacing:.5px;color:#fff;text-transform:uppercase;margin-bottom:28px}
.fnav a{display:block;width:178px;font-size:12px;padding:0 0 7px;margin-bottom:7px;border-bottom:1px solid #6b6d71}
.fnav a:last-child{border:none}
.fcol p{font-size:12px;line-height:1.55}
.email-field{width:188px;height:31px;margin-top:24px;background:#e6e7e8;border:2px solid #9a9c9f;font-size:10px;color:#999;padding:8px 6px}
.btn-join{margin-top:12px;width:70px;height:19px;background:var(--blue);color:#fff;font-size:10.5px;font-weight:500;display:flex;align-items:center;justify-content:center}
.testi{position:relative;padding-left:20px;margin-bottom:14px;width:200px}
.testi q{font-style:italic;font-size:11.5px;line-height:1.55;quotes:none}
.testi .qmark{position:absolute;left:0;top:-6px;font-size:28px;font-family:Georgia,serif;color:#fff}
.testi .by{font-size:11.5px;margin-top:8px}
.testi .by em{margin-left:10px;font-weight:700}
.testi .btn-more{margin-top:7px;width:52px}
.contact-line{display:flex;gap:10px;font-size:12px;line-height:1.55;margin-bottom:8px}
.contact-line svg{width:11px;height:12px;fill:#fff;flex:none;margin-top:3px}
.fcol .social span{width:15px;height:15px}
.bottombar{left:0;top:2245px;width:1200px;height:66px;background:var(--footer-dark)}
.footer-brand{position:absolute;left:182px;top:16px;display:flex;align-items:center;gap:6px;font-weight:700;font-size:14px;line-height:1.1;color:#fff}
.footer-brand .mark{width:12px;height:12px;border-radius:50%;background:#fff;flex:none}
.copyright{position:absolute;left:294px;top:26px;font-size:11.5px;color:#9b9ea2}
.btn-top{position:absolute;left:918px;top:22px;width:84px;height:19px;background:var(--blue);color:#fff;font-size:9.5px;font-weight:700;display:flex;align-items:center;justify-content:center;gap:4px}
</style>
</head>
<body>

<div class="abs topbar">
  <div class="abs item" style="left:176px"><svg viewBox="0 0 24 24"><path d="M6.6 10.8a15 15 0 0 0 6.6 6.6l2.2-2.2a1 1 0 0 1 1-.25 11.4 11.4 0 0 0 3.6.57 1 1 0 0 1 1 1V20a1 1 0 0 1-1 1A17 17 0 0 1 3 4a1 1 0 0 1 1-1h3.5a1 1 0 0 1 1 1c0 1.25.2 2.45.57 3.570a1 1 0 0 1-.25 1z"/></svg>555-210-4480</div>
  <div class="abs item" style="left:314px"><svg viewBox="0 0 24 24"><path d="M2 5h20v14H2zm2 2v.5l8 5 8-5V7z"/></svg>info@hearthsidecare.com</div>
  <div class="abs item" style="left:506px"><svg viewBox="0 0 24 24"><path d="M12 2a7 7 0 0 0-7 7c0 5 7 13 7 13s7-8 7-13a7 7 0 0 0-7-7zm0 9.5A2.5 2.5 0 1 1 12 6.5a2.5 2.5 0 0 1 0 5z"/></svg>Lorem Ipsum Street, Lorem Ipsum</div>
  <div class="abs item" style="left:888px">Follow Us <div class="social"><span></span><span></span><span></span><span></span></div></div>
</div>

<header class="abs header"></header>
<div class="abs brand"><span class="mark"></span><span>Hearthside<br>Home Care</span></div>
<nav class="abs nav">
  <a class="active" href="#">Home</a><a href="#">About Us</a><a href="#">Services</a><a href="#">Resources</a><a href="#">FAQ</a><a href="#">Employment</a><a href="#">Contact</a>
</nav>
<div class="abs header-rule"></div>

<section class="abs hero" role="img" aria-label="Photo of a smiling caregiver in blue scrubs facing an elderly woman"></section>
<div class="abs hero-caption">Lorem Ipsum Dolor Sit Amet</div>
<p class="abs hero-sub">Duis aute irure dolor in reprehenderit in voluptate velit esse cillum dolore eu fugiat nulla pariatur...</p>
<div class="abs hero-arrow" style="left:32px"><svg viewBox="0 0 14 14"><path d="M9 2 4 7l5 5"/></svg></div>
<div class="abs hero-arrow" style="left:1122px"><svg viewBox="0 0 14 14"><path d="M5 2l5 5-5 5"/></svg></div>
<div class="abs hero-bar"></div>

<div class="abs appointment">
  <h1>Tender Loving Home Care For<br>Your Loved Ones</h1>
  <a class="btn-appoint" href="#"><svg viewBox="0 0 24 24"><circle cx="12" cy="7" r="5"/><path d="M2 23c0-6 4.5-9 10-9s10 3 10 9z"/></svg>Make an Appointment</a>
</div>

<div class="abs feature" style="left:172px">
  <div class="icon"><svg viewBox="0 0 24 24"><path d="M12 3 2 12h3v9h5v-6h4v6h5v-9h3z"/></svg></div>
  <h3>About Hearthside Home Care</h3>
  <p>vero eos et accusamus et iusto odio dignissimos ducimus qui blanditiis...</p>
  <a class="btn-more" href="#">MORE</a>
</div>
<div class="abs feature" style="left:462px">
  <div class="icon"><svg viewBox="0 0 24 24"><path d="M12 21s-8-5-8-11a4.5 4.5 0 0 1 8-3 4.5 4.5 0 0 1 8 3c0 6-8 11-8 11z"/></svg></div>
  <h3>The Services We Provide</h3>
  <p>Nam libero tempore, cum soluta nobis est eligendi optio cumque nihil impedit...</p>
  <a class="btn-more" href="#">MORE</a>
</div>
<div class="abs feature" style="left:752px">
  <div class="icon"><svg viewBox="0 0 24 24"><path d="M10 4h4v6h6v4h-6v6h-4v-6H4v-4h6z"/></svg></div>
  <h3>Care and Support for Older People</h3>
  <p>Temporibus autem quibusdam et aut officiis debitis aut rerum necessitatibus...</p>
  <a class="btn-more" href="#">MORE</a>
</div>

<div class="abs caregiver">
  <p>Become a care giver..</p>
  <a class="btn-apply" href="#">APPLY TODAY</a>
</div>

<h2 class="abs intro">Lorem Ipsum Dolor Sit Amet, Consectetur Adipisicing Elit, Ed Do Eiusmod<br>Tempor Incididunt Ut Labore Et Dolore Magna Aliqua</h2>

<article class="abs card" style="left:174px">
  <div class="photo" role="img" aria-label="Photo of a caregiver sharing a laugh with an elderly woman" style="background:linear-gradient(135deg,#d9a9a0,#efe2da 60%,#b59b8f)"></div>
  <h4>The Help Your Loved One Deserves</h4>
  <p>Sed ut perspiciatis unde omnis iste natus error sit voluptatem accusantium...</p>
  <a class="btn-more" href="#">MORE</a>
</article>
<article class="abs card" style="left:396px">
  <div class="photo" role="img" aria-label="Photo of a caregiver serving a meal to an elderly woman" style="background:linear-gradient(135deg,#e8d3b0,#f3ecd9 55%,#b7b86e)"></div>
  <h4>Making the Right<br>Decision</h4>
  <p>Eaque ipsa quae ab illo inventore veritatis et quasi architecto beatae vitae...</p>
  <a class="btn-more" href="#">MORE</a>
</article>
<article class="abs card" style="left:619px">
  <div class="photo" role="img" aria-label="Photo of an elderly man reading with a caregiver" style="background:linear-gradient(135deg,#8a5a3e,#c9a589 55%,#e6ddd3)"></div>
  <h4>Home Care Could Be the Answer You've Been Looking For</h4>
  <p>Nemo enim ipsam voluptatem quia voluptas sit aspernatur aut odit aut fugi...</p>
  <a class="btn-more" href="#">MORE</a>
</article>
<article class="abs card" style="left:839px">
  <div class="photo" role="img" aria-label="Photo of an elderly man with a drink beside a smiling caregiver" style="background:linear-gradient(135deg,#9fc2d8,#eadfd6 55%,#c79a7c)"></div>
  <h4>A Little Help Can Make A Big Difference</h4>
  <p>Consequuntur magni dolores eos qui ratione voluptatem sequi nesciunt...</p>
  <a class="btn-more" href="#">MORE</a>
</article>

<section class="abs panel" style="left:172px">
  <div class="panel-head"><h2>TWEETS</h2><span class="btn-follow">Follow</span></div>
  <div class="tweet" style="top:76px">
    <div class="who"><i></i>Hearthside Home Care</div>
    <div class="body"><b>Hearthside Home Care</b><br>Quis autem vel eum iure reprehenderit qui in ea voluptate velit esse quam nihil<span class="meta">Expand</span></div>
    <span class="date">16th Nov</span>
  </div>
  <div class="tweet" style="top:168px">
    <div class="who"><i></i>Hearthside Home Care</div>
    <div class="body"><b>Hearthside Home Care</b><br>voluptatum deleniti atque corrupti quos dolores et quas molestias excepturi sint<span class="meta">Retweeted by Hearthside Home Care</span><span class="meta">Expand</span></div>
    <span class="date">10th Nov</span>
  </div>
  <div class="tweet" style="top:278px">
    <div class="who"><i></i>Hearthside Home Care</div>
    <div class="body"><b>Hearthside Home Care</b><br>Temporibus autem quibusdam et aut officiis debitis aut rerum necessitatibus<span class="meta">Expand</span></div>
    <span class="date">4th Nov</span>
  </div>
</section>

<section class="abs panel" style="left:617px">
  <div class="panel-head"><h2>LATEST NEWS</h2><a class="btn-view" href="#">VIEW ALL</a></div>
  <div class="news" style="top:76px">
    <div class="thumb" role="img" aria-label="Photo of hands held together"></div>
    <div class="date">20th Nov<br>2013</div>
    <h5>Excepteur Sint Occaecat Cupidatat Non Proident</h5>
    <small>3 Comments</small>
    <p>Neque porro quisquam est, qui dolorem ipsum quia dolor sit amet, consectetur, adipisci velit, sed quia non numquam eius modi...</p>
  </div>
  <div class="news" style="top:228px">
    <div class="thumb" role="img" aria-label="Photo of a caregiver with an elderly woman" style="background:linear-gradient(135deg,#c9d7de,#d8b7a4)"></div>
    <div class="date">4th Nov<br>2013</div>
    <h5>Temporibus Autem Quibusdam Et Aut Officiis Debitis</h5>
    <small>2 Comments</small>
    <p>Itaque earum rerum hic tenetur a sapiente delectus, ut aut reiciendis voluptatibus maiores alias consequatur aut perferendis doloribus asperiores repellat...</p>
  </div>
</section>

<footer class="abs footer">
  <div class="fcol" style="left:176px">
    <h6>Navigations</h6>
    <div class="fnav"><a href="#">Home</a><a href="#">About Us</a><a href="#">Services</a><a href="#">Resources</a><a href="#">FAQ</a><a href="#">Employment</a><a href="#">Contact</a></div>
  </div>
  <div class="fcol" style="left:393px">
    <h6>Newslatter Signup</h6>
    <p style="width:195px">By Subscribing to Our Mailing List You Will Always Get Updated News From Us.</p>
    <div class="email-field">EMAIL</div>
    <a class="btn-join" href="#">JOIN US</a>
  </div>
  <div class="fcol" style="left:613px">
    <h6>Testimonials</h6>
    <div class="testi"><span class="qmark">&ldquo;</span><q>Nam libero tempore, cum soluta nobis est eligendi...</q><div class="by">By Marla Quinn<em>14th Nov</em></div><a class="btn-more" href="#">MORE</a></div>
    <div class="testi"><span class="qmark">&ldquo;</span><q>Quo minus id quod maxime placeat facere possimus...</q><div class="by">By Marla Quinn<em>14th Nov</em></div><a class="btn-more" href="#">MORE</a></div>
  </div>
  <div class="fcol" style="left:834px">
    <h6>Contact</h6>
    <div class="contact-line"><svg viewBox="0 0 24 24"><path d="M12 2a7 7 0 0 0-7 7c0 5 7 13 7 13s7-8 7-13a7 7 0 0 0-7-7zm0 9.5A2.5 2.5 0 1 1 12 6.5a2.5 2.5 0 0 1 0 5z"/></svg>Lorem Ipsum Street,<br>Lorem Ipsum</div>
    <div class="contact-line"><svg viewBox="0 0 24 24"><path d="M6.6 10.8a15 15 0 0 0 6.6 6.6l2.2-2.2a1 1 0 0 1 1-.25 11.4 11.4 0 0 0 3.6.57 1 1 0 0 1 1 1V20a1 1 0 0 1-1 1A17 17 0 0 1 3 4a1 1 0 0 1 1-1h3.5a1 1 0 0 1 1 1c0 1.25.2 2.45.57 3.57a1 1 0 0 1-.25 1z"/></svg>555-210-4481</div>
    <div class="contact-line"><svg viewBox="0 0 24 24"><path d="M2 5h20v14H2zm2 2v.5l8 5 8-5V7z"/></svg>info@hearthsidecare.com</div>
    <h6 style="margin:22px 0 12px">Follow Us</h6>
    <div class="social"><span></span><span></span><span></span><span></span></div>
  </div>
</footer>

<div class="abs bottombar">
  <div class="footer-brand"><span class="mark"></span><span>Hearthside<br>Home Care</span></div>
  <p class="copyright">copyright2013@hearthsidecare.com. All rights reserved</p>
  <a class="btn-top" href="#">TO THE TOP <svg width="8" height="9" viewBox="0 0 8 9"><path d="M4 0 0 4h2.5v5h3V4H8z" fill="#fff"/></svg></a>
</div>

</body>
</html>
```